Wine label for South African wine

modern, creative wine label name: Dravenholt The Varnex-Bund GmbH - International Wines one of the leading independent providers of inexpensive wines from around the world. The company focuses entirely on this dynamic, constantly evolving wine market, and our customers can therefore take full advantage of a complete supply chain management for themselves, including: * http://www.varnexbund.example/img/rebe.jpg procuring wines from the major producing regions around the globe * logistics and processing * wage filling and packaging * dealcoholization of wines for gastronomic purposes * design of exclusive client and proprietary brands, the target market / target group: the International market design Features; Modern, simple, meaningful, unique; Colors: gold, black, red;

Target Market(s)

Off Trade

Industry/Entity Type

Union

Font styles to use
Serif
Script

Requirements
Must have
• Modern, simple, meaningful, unique colors: gold, black, red varieties: Cab Sauv, Chard, Chenin, Merlot, Merlot Rose, Pinotage, Pinotage Rose, Shiraz, Red, Rose, White Non transparent max. Size: 12 x 9 cm data on VE: name brand, variety, country; WITHOUT Year

```html
<!DOCTYPE html>
<html lang="en">
<head>
<meta charset="utf-8">
<title>Merlot Rose – Wine Label</title>
<link rel="stylesheet" href="https://fonts.googleapis.com/css2?family=EB+Garamond:wght@400;500&family=Pinyon+Script&display=swap">
<style>
  :root {
    --page: #ffffff;
    --label: #ffffff;
    --frame: #2a2a2a;
    --ink: #2b2b2b;
    --gold: #c0933a;
    --gold-light: #d9b463;
    --gold-deep: #a77a26;
    --wine-red: #c3202e;
    --rule: #8a8a8a;
  }
  * { margin: 0; padding: 0; box-sizing: border-box; }
  html, body {
    width: 1200px;
    height: 600px;
    overflow: hidden;
    background: var(--page);
  }
  .canvas {
    position: relative;
    width: 1200px;
    height: 600px;
  }
  .label {
    position: absolute;
    left: 384px;
    top: 16px;
    width: 432px;
    height: 568px;
    background: var(--label);
    border: 2px solid var(--frame);
  }
  .label__origin {
    position: absolute;
    top: 36px;
    left: 0;
    width: 100%;
    text-align: center;
    font-family: "EB Garamond", Georgia, serif;
    font-size: 20px;
    color: var(--ink);
    letter-spacing: 0.3px;
  }
  .label__emblem {
    position: absolute;
    left: 124px;
    top: 60px;
    width: 184px;
    height: 304px;
    border-radius: 46% 46% 40% 40% / 38% 38% 50% 50%;
    background: radial-gradient(ellipse at 50% 40%, var(--gold-light) 0%, var(--gold) 55%, var(--gold-deep) 100%);
  }
  .label__variety {
    position: absolute;
    top: 412px;
    left: 0;
    width: 100%;
    text-align: center;
    font-family: "EB Garamond", Georgia, serif;
    font-weight: 400;
    font-size: 68px;
    line-height: 1;
    color: var(--wine-red);
  }
  .label__rule {
    position: absolute;
    top: 512px;
    left: 90px;
    width: 250px;
    height: 0;
    border-top: 1.5px solid var(--rule);
  }
  .label__region {
    position: absolute;
    top: 518px;
    left: 0;
    width: 100%;
    text-align: center;
    font-family: "Pinyon Script", cursive;
    font-size: 26px;
    font-weight: 700;
    color: var(--ink);
    -webkit-text-stroke: 0.4px var(--ink);
  }
</style>
</head>
<body>
  <main class="canvas">
    <section class="label">
      <p class="label__origin">Wine Of South Africa</p>
      <div class="label__emblem" role="img" aria-label="Gold emblem of a lion's head"></div>
      <h1 class="label__variety">Merlot Rose</h1>
      <div class="label__rule"></div>
      <p class="label__region">Western Cape</p>
    </section>
  </main>
</body>
</html>
```